Skin care manufacturer looking for packaging design for new skin care brand.

We need a design and logo for a skin care brand to be sold at retail stores and online in the United States and Europe. The design will be for 1.7oz - 2oz serums that will not have a retail box. The name of the brand is Orvia Lune and should be a luxurious brand that is approachable. The brand will consist of 4 face serums - Vitamin C, Collagen, Retinol and Hyaluronic Acid that all contain Dead Sea Minerals. Images shown are for inspiration only. Color of bottles can be varied based on design and bottles can be screen printed or labeled.

```html
<!DOCTYPE html>
<html lang="en">
<head>
<meta charset="utf-8">
<title>Orvia Lune — Serum Collection</title>
<link href="https://fonts.googleapis.com/css2?family=Josefin+Sans:wght@300;400;600&display=swap" rel="stylesheet">
<style>
  :root {
    --canvas: #ffffff;
    --ink: #222222;
    --band: #262626;
    --band-text: #ffffff;
    --top: #f4f4f4;
    --teal-1: #d3ebe0; --teal-2: #86cfbb; --teal-3: #17a192; --teal-4: #0a6c62;
    --amber-1: #fbe4d4; --amber-2: #f5b48e; --amber-3: #ec8f4a; --amber-4: #b5531a;
    --rose-1: #f4d0d6; --rose-2: #e4939e; --rose-3: #d05c6a; --rose-4: #8c1427;
    --sky-1: #c6e5ef; --sky-2: #82c3db; --sky-3: #2b8fbe; --sky-4: #0a497a;
  }
  * { margin: 0; padding: 0; box-sizing: border-box; }
  html, body {
    width: 1200px; height: 750px; overflow: hidden;
    background: var(--canvas);
    font-family: "Josefin Sans", sans-serif;
    color: var(--ink);
  }
  .collection { position: relative; width: 1200px; height: 750px; }
  .label {
    position: absolute; top: 269px; width: 152px; height: 343px;
    border-radius: 3px 3px 5px 5px;
    text-align: center;
    overflow: hidden;
  }
  .label::after {
    content: ""; position: absolute; inset: 0;
    background: linear-gradient(90deg, rgba(0,0,0,0.07) 0%, rgba(0,0,0,0) 14%, rgba(0,0,0,0) 80%, rgba(0,0,0,0.1) 100%);
    pointer-events: none;
  }
  .label--collagen { left: 186px; background: linear-gradient(180deg, var(--top) 0%, #fbfbfb 40%, var(--teal-1) 60%, var(--teal-2) 76%, var(--teal-3) 94%, var(--teal-4) 100%); }
  .label--vitamin  { left: 405px; background: linear-gradient(180deg, var(--top) 0%, #fbfbfb 40%, var(--amber-1) 55%, var(--amber-2) 76%, var(--amber-3) 93%, var(--amber-4) 100%); }
  .label--retinol  { left: 623px; background: linear-gradient(180deg, var(--top) 0%, #fbfbfb 44%, var(--rose-1) 62%, var(--rose-2) 78%, var(--rose-3) 93%, var(--rose-4) 100%); }
  .label--hyaluron { left: 841px; background: linear-gradient(180deg, var(--top) 0%, #fbfbfb 44%, var(--sky-1) 62%, var(--sky-2) 76%, var(--sky-3) 93%, var(--sky-4) 100%); }

  .brand {
    position: absolute; top: 88px; left: 0; right: 0;
    font-weight: 300; font-size: 13px; letter-spacing: 0.5px;
  }
  .title {
    position: absolute; top: 165px; left: 0; right: 0;
    font-weight: 400; font-size: 13px; line-height: 15px;
    text-transform: uppercase;
  }
  .type-band {
    position: absolute; top: 200px; left: 21px; width: 110px; height: 12px;
    background: var(--band); color: var(--band-text);
    font-size: 9.5px; line-height: 13px; letter-spacing: 1px;
  }
  .strength {
    position: absolute; top: 231px; left: 0; right: 0;
    font-size: 10px; font-weight: 600;
  }
  .claims {
    position: absolute; top: 249px; left: 14px; right: 14px;
    font-size: 6px; line-height: 7px; text-transform: uppercase;
  }
  .volume {
    position: absolute; top: 303px; left: 21px;
    font-size: 7px; font-weight: 600;
  }
  .label--vitamin .title { top: 163px; }
  .label--vitamin .type-band { top: 198px; }
  .label--retinol .title { top: 167px; }
</style>
</head>
<body>
<main class="collection">
  <section class="label label--collagen">
    <p class="brand">Orvia Lune</p>
    <h2 class="title">Phyto Plump<br>Collagen</h2>
    <p class="type-band">SERUM</p>
    <p class="claims">A light, refreshing collagen serum with a vegan formla, dead minirals</p>
    <p class="volume">29ML</p>
  </section>

  <section class="label label--vitamin">
    <p class="brand">Orvia Lune</p>
    <h2 class="title">Brightening<br>Vitamin C</h2>
    <p class="type-band">SERUM</p>
    <p class="strength">3.5%</p>
    <p class="claims" style="top:249px">Vitamin C + Niacinamide<br>+ Salicylic Acid</p>
    <p class="volume">29ML</p>
  </section>

  <section class="label label--retinol">
    <p class="brand">Orvia Lune</p>
    <h2 class="title">Skin Renewal<br>Retinol</h2>
    <p class="type-band">SERUM</p>
    <p class="claims" style="left:8px;right:8px">Refines skin textures, intensive<br>acne care, revives radiance</p>
    <p class="volume">29ML</p>
  </section>

  <section class="label label--hyaluron">
    <p class="brand">Orvia Lune</p>
    <h2 class="title">Ultra Pure<br>Hyaluronic Acid</h2>
    <p class="type-band">SERUM</p>
    <p class="claims">Ultra hydrating, replumping,<br>anti aging, repairing</p>
    <p class="volume">29ML</p>
  </section>
</main>
</body>
</html>
```